Pebble-Vane Brochure

Hello,

I want a "printed" version of the www.Pebble-Vane.net web site, so I can send it to prospect customers by physical mail.

Full Color, Letter Size paper and maximum of 8 pages.

If you need any additional information please let me know.

```html
<!DOCTYPE html>
<html lang="en">
<head>
<meta charset="utf-8">
<title>Pebble-Vane Brochure</title>
<link href="https://fonts.googleapis.com/css2?family=Audiowide&family=Roboto+Condensed:ital,wght@0,300;0,400;0,700;1,700&display=swap" rel="stylesheet">
<style>
:root{
  --blue:#0a96d8;
  --teal:#5bc8d4;
  --ink:#2a2a2a;
  --soft:#3d3d3d;
  --rule:#0a96d8;
  --page-right:#f4f4f5;
}
*{margin:0;padding:0;box-sizing:border-box}
html,body{width:1200px;height:777px;overflow:hidden;background:#fff}
body{font-family:"Roboto Condensed",Arial,sans-serif;color:var(--soft);position:relative}
.spread{position:relative;width:1200px;height:777px}
.page-left{position:absolute;left:0;top:0;width:600px;height:777px;background:#fff}
.page-right{position:absolute;left:600px;top:0;width:600px;height:777px;background:linear-gradient(90deg,#e4e4e6 0,var(--page-right) 30px,#fbfbfb 100%)}
.title{position:absolute;top:36px;font-family:"Audiowide",sans-serif;color:var(--blue);font-size:23.5px;letter-spacing:-.2px;font-weight:400;line-height:30px}
.block{position:absolute;font-size:8.6px;line-height:10.6px;font-weight:300;color:var(--soft)}
.block h3{font-size:9.3px;font-weight:700;color:var(--ink);text-transform:uppercase;line-height:11px}
.block .lead{font-size:9.4px;font-weight:400;color:var(--ink);line-height:12px}
.block p{margin:0}
.rule{position:absolute;height:1px;background:var(--rule)}
.note{position:absolute;font-size:8.6px;line-height:10.6px;font-weight:300;color:var(--soft)}
.note.big{font-size:9.8px;line-height:12px}
.rblock{position:absolute;font-size:9.9px;line-height:12px;font-weight:300;color:var(--ink)}
.rblock h3{font-size:9.3px;font-weight:700;text-transform:uppercase;line-height:12px;margin-bottom:13px}
.rblock p{margin-bottom:12px}
.rblock ul{list-style:none}
.rblock li{position:relative;padding-left:8px}
.rblock li::before{content:"•";position:absolute;left:0;color:var(--blue)}
.rblock.small{font-size:8.7px;line-height:10.6px}
.rblock.small h3{margin-bottom:0}
.rblock.small .lead{font-size:9.6px;line-height:12px}
.rblock.small li{padding-left:16px}
.rblock.small li::before{left:0}
.facts{position:absolute;width:227px;font-size:10.3px;font-weight:400;color:#fff}
.facts div{display:flex;align-items:center;padding:0 17px;line-height:12px}
.facts .lt{background:var(--teal)}
.facts .dk{background:var(--blue)}
.url{position:absolute;left:1066px;top:733px;font-size:11px;font-weight:700;font-style:italic;color:var(--blue)}
</style>
</head>
<body>
<div class="spread">
  <section class="page-left">
    <h1 class="title" style="left:33px">cloud services</h1>

    <div class="block" style="left:35px;top:75px;width:265px">
      <h3>Server Virtualization</h3>
      <p class="lead">You may create Virtual Servers with the following Operating systems</p>
      <p>Fenmark Server 2.012 R2 – GUI<br>Fenmark Server 2.012 R2 – CORE<br>Crimsoncap Enterprise Lynex 7<br>Sorel Enterprise Lynex 12<br>Corvia 6.7 and 7.0<br>Augur Lynex 7<br>Open Sorel 42<br>Brindle 14 LTS</p>
    </div>
    <div class="block" style="left:315px;top:75px;width:238px">
      <h3>Backup &amp; Recovery</h3>
      <p class="lead">With our integrated backup system you will be able to keep</p>
      <p>your data protected.<br>Backup any file or folder of a virtual server.<br>Snapshots to backup and restore an entire virtual machine.<br>Copy an entire virtual machine (Cloning)<br>Automatic backup scheduling<br>Ability to download the backup files or make them available within a virtual server.<br>Control the storage space dedicated for backups.</p>
    </div>
    <div class="rule" style="left:34px;top:189px;width:529px"></div>
    <p class="note" style="left:35px;top:193px;width:528px">You will be able to manage your virtual servers (including access to the server's console) directly from any modern web browser without installing any client software.</p>

    <div class="block" style="left:34px;top:228px;width:275px">
      <h3>Server Monitoring</h3>
      <p class="lead">We have integrated the famous AGAVE system into our cloud platform.</p>
      <p>Monitor the health of your virtual machines.<br>Gather cpu, ram, network and disk space statistics for all your virtual servers.<br>Generate alerts using the TLIMIT plugin.<br>Monitor also the behavior of your physical hardware.</p>
    </div>
    <div class="block" style="left:318px;top:228px;width:252px">
      <h3>VLAN Definitions</h3>
      <p>A VLAN is a private broadcast domain at the ARP (switch) level.<br>Isolate groups of virtual servers from each other to avoid the possibility of sniffing private communications.<br>Allows to host different customer networks within the same cloud without security concerns.<br>VLANs can be distributed through different Pebble-Vanes.</p>
    </div>
    <div class="rule" style="left:34px;top:309px;width:529px"></div>
    <p class="note" style="left:34px;top:315px">You can create isolated virtual networks for different customers.</p>

    <div class="block" style="left:34px;top:338px;width:262px">
      <h3>HTTP Acceleration</h3>
      <p class="lead">The websites you host will benefit from the following features of the HTTP Accelerator engine integrated into the Pebble-Vane platform:</p>
      <p>Page and element caching to avoid overloading your virtual web servers.<br>HTTP Load Balancing to distribute the site requests into various virtual machines.<br>SSL/TLS Encryption at the physical hardware level.<br>SSL Certificate management.<br>Firewall integration: You may decide which IP addresses can access any particular web site.<br>Web site segmentation, different areas of a web site may be served by different virtual machines</p>
    </div>
    <div class="block" style="left:315px;top:338px;width:248px">
      <h3>Firewall Filtering</h3>
      <p class="lead">The Pebble-Vane system offers a firewall filtering mechanism integrated with your private cloud.</p>
      <p>IPv4 and IPv6 filters to define which addresses can or cannot access services in your virtual machines.<br>Black Listing of malicious IP addresses:, when you detect an attacker you may include his address in the black list so any access to your cloud will be denied.<br>UDP, TCP and ICMP Services can be used in firewall rules.<br>You may define firewall rules per virtual machine and reuse them in other VMs if necessary.<br>Web Management interface to define objects, services and rules</p>
    </div>
    <div class="rule" style="left:34px;top:476px;width:529px"></div>
    <p class="note big" style="left:34px;top:482px">You can handle multiple web sites with high-level security<br>IPv6 ready!</p>

    <div class="block" style="left:34px;top:521px;width:262px">
      <h3>Site to Site VPN</h3>
      <p>Useful to interconnect two networks permanently.<br>It uses the IPSEC protocol to keep your data secured.<br>You may connect your office/company network with the Pebble-Vane so your client computers can access the virtual servers transparently.<br>Requires a Fixed IP address and a router supporting the IPSEC protocol</p>
    </div>
    <div class="block" style="left:313px;top:521px;width:250px">
      <h3>Remote Management VPN</h3>
      <p>Used to create temporary secure connections to your servers in order to perform management procedures.<br>Useful to access servers with no open ports in order to increase security.<br>Uses the L2TP / IPSEC vpn protocol.<br>Can be accessed from Fenmark , Macro or Lynex clients.<br>Useful also for mobile clients with no fixed IP Address.</p>
    </div>
    <div class="rule" style="left:34px;top:605px;width:529px"></div>
    <div class="block" style="left:40px;top:613px;width:500px">
      <h3 style="font-size:8.4px">Virtual Private Networking</h3>
      <p>Connect to your virtual machines from outside the cloud even if they have no public IP access!</p>
    </div>

    <div class="block" style="left:34px;top:650px;width:262px">
      <h3>Virtual SAN</h3>
      <p>Ability to create shared storage blocks.<br>SMB, NFS and iSCSI protocols supported.<br>All virtual machines within a VLAN can share data using a virtual SAN.<br>Fenmark Cluster supported through the iSCSI protocol.</p>
    </div>
    <div class="block" style="left:314px;top:653px;width:250px">
      <h3>Sentry I.P.S</h3>
      <p>New generation firewall with Intrusion Prevention System<br>Detects threats and attacks by analyzing network traffic in real time.<br>Easy to use web interface to browse all the alerts generated by the IPS.<br>Firewall integration can reject suspicious connections without user intervention.</p>
    </div>
    <div class="rule" style="left:34px;top:725px;width:529px"></div>
    <div class="block" style="left:34px;top:731px;width:500px">
      <h3 style="font-size:8.4px">Automatic Upgrades</h3>
      <p>The Intrusion Prevention System is updated every day to keep your system protected from the latest threads.</p>
    </div>
  </section>

  <section class="page-right">
    <h1 class="title" style="left:42px">vane's infrastructure</h1>
  </section>

  <div class="rblock" style="left:644px;top:94px;width:226px">
    <h3>Pebble-Vane Hardware</h3>
    <p>At the end, a virtual machine needs physical hardware to run. In a public cloud you don't know in which server your virtual machine will run or how many customers will share the hardware with you.</p>
    <p style="margin-bottom:16px">In our private cloud you have dedicated servers to host your virtual machines: that means only you will control how resources are used.</p>
    <p>Each Pebble-Vane includes:</p>
    <p>CPU: Arvo Optima 6XXX Series processors.<br>Memory: Twice the RAM of your plan<br>RAID 10 Cloud Storage with SSD Acceleration<br>(High performance, unlimited iops)</p>
  </div>

  <div class="rblock" style="left:917px;top:94px;width:250px">
    <h3 style="margin-left:7px">Internet Connectivity</h3>
    <p style="margin-left:7px;width:235px">Do not worry about internet connection outages, to guarantee redundancy and permanent availability of service, we have 8 internet link providers</p>
    <ul style="margin-bottom:12px">
      <li>Tier Nine</li><li>TWNC</li><li>Globe Span</li><li>GXT</li><li>NXT</li><li>Cogence</li><li>Seaspine</li><li>XQ transit</li>
    </ul>
    <p style="margin-left:7px;width:235px">Every Pebble-Vane is powered with 100 Mbps of Internet bandwidth and unlimited data transfer in the Enterprise configuration.</p>
  </div>

  <div class="facts" style="left:633px;top:338px">
    <div class="lt" style="height:23.6px">100% power uptime since 2011</div>
    <div class="dk" style="height:23.6px">100% network uptime since 2014</div>
    <div class="lt" style="height:23.6px">242 Gbps network capacity</div>
    <div class="dk" style="height:23.6px">N + 2 redudant CRAC cooling</div>
  </div>
  <div class="facts" style="left:912px;top:338px">
    <div class="lt" style="height:23.6px;padding-left:23px">Battery and generator power backups</div>
    <div class="dk" style="height:47px;padding-left:23px">8 internet connectivity providers; Tier Nine,<br>TWNC, Globe Span, GXT, Comlink, NXT,<br>Cogence, Seaspine, XQ transit</div>
    <div class="lt" style="height:23.6px;padding-left:23px">Privately peared with 300+ networks</div>
    <div class="dk" style="height:23.6px;padding-left:23px">DDOS mitigation appliances available</div>
  </div>

  <div class="rblock small" style="left:645px;top:492px;width:232px">
    <h3>Hardware Redundancy</h3>
    <p class="lead">You can be sure you are not just renting a server.<br>You are contracting a a full featured Private Cloud service.</p>
    <ul style="margin-top:-2px">
      <li style="margin-bottom:10px">If for any reason your physical hardware fails, we will provide immediately a fail over server to resume your service.</li>
      <li style="margin-bottom:10px">Do not worry about your data, our Cloud Storage system keeps up to four online copies of your virtual disks to handle any kind of hardware failure.</li>
      <li>Thanks to this architecture we can guarantee 99,9% availability per month.</li>
    </ul>
  </div>

  <div class="rblock small" style="left:924px;top:492px;width:246px">
    <h3>Cloud Services</h3>
    <p class="lead" style="margin-bottom:2px">But you will not receive just a server, you will get a completely functional and ready to use Virtual Datacenter with great features like:</p>
    <ul>
      <li>Creating Fenmark or Lynex virtual machines with just a few clicks.</li>
      <li>Web managed firewall and I.P.S.</li>
      <li>VPN connectivity.</li>
      <li>Statistics and monitoring system.</li>
      <li>Web acceleration (HTTP cache + load balancing)</li>
      <li>VLAN creation.</li>
      <li>Integrated backup system.</li>
      <li>7 x 24 support.</li>
    </ul>
  </div>

  <div class="rule" style="left:633px;top:740px;width:416px"></div>
  <div class="url">www.Pebble-Vane.net</div>
</div>
</body>
</html>
```